I have looking for nice Photo for my Business Cards , see below details I justed send.

Please see my Website Link , It should be up and running my late tonight or tomorrow morning.

http://www.coralbreezeescapes.net

Travel & Toursim

Company Name: Coral Breeze Escapes

If you look at my Website it will show you photos that keep changing at the top. I want something like that or if you have some samples to show me.
Looking for a beach with sand and maybe having somebody resting on the beach with a drink or reading.

Let me know what you think.

Also what will be the cost hopefully you already got some photos to show me. I want my business Card to be glossy.

Business

Contact: Delphine Orvak
Mobile: 0437 912 654
Email: delphine@coralbreezetrips.com
Website: www.coralbreezeescapes.net

• Company Name: Coral Breeze Escapes
Contact: Delphine Orvak
Mobile: 0437 912 654

```html
<!DOCTYPE html>
<html lang="en">
<head>
<meta charset="utf-8">
<title>Coral Breeze Escapes – Business Cards</title>
<link rel="stylesheet" href="https://fonts.googleapis.com/css2?family=Questrial&family=Varela+Round&display=swap">
<style>
  :root {
    --backdrop: #3b302b;
    --card-white: #f7f6f2;
    --sky-top: #4f9fe6;
    --sky-light: #bfe0f7;
    --sea-turquoise: #3cc6cf;
    --sea-deep: #1f8fb3;
    --sand: #f3efe6;
    --brand-grey: #6f7478;
    --contact-blue: #3aa2d9;
    --icon-dark: #2b2b2b;
  }
  * { box-sizing: border-box; margin: 0; padding: 0; }
  html, body {
    width: 1200px; height: 561px; overflow: hidden;
    background: var(--backdrop);
  }
  .canvas {
    position: relative; width: 1200px; height: 561px;
    display: flex; align-items: center; justify-content: center; gap: 40px;
  }
  .card {
    position: relative; width: 530px; height: 310px;
    border-radius: 18px; overflow: hidden;
    background: var(--card-white);
    box-shadow: 0 10px 24px rgba(0,0,0,.45);
  }
  /* Front: contact side */
  .front-photo {
    position: absolute; inset: 0 0 34% 0;
    background: linear-gradient(180deg, var(--sky-top) 0%, var(--sky-light) 34%, var(--sea-turquoise) 52%, #7fdcd9 74%, var(--sand) 100%);
  }
  .front-sand {
    position: absolute; left: 0; right: 0; bottom: 0; height: 42%;
    background: linear-gradient(180deg, rgba(243,239,230,0) 0%, var(--sand) 30%, #ebe7de 100%);
  }
  .front-brand {
    position: absolute; left: 152px; top: 150px;
    font-family: "Questrial", sans-serif; font-size: 19px; letter-spacing: .5px;
    color: var(--brand-grey);
  }
  .contact-name {
    position: absolute; left: 26px; bottom: 48px;
    font-family: "Varela Round", sans-serif; font-size: 18px;
    color: var(--contact-blue); font-weight: 700;
  }
  .contact-list {
    position: absolute; right: 18px; top: 152px;
    list-style: none; text-align: right;
    font-family: "Varela Round", sans-serif; font-size: 13px; line-height: 22px;
    color: var(--contact-blue);
  }
  .contact-list li { display: flex; justify-content: flex-end; align-items: center; gap: 10px; }
  .contact-list li:first-child { margin-bottom: 4px; }
  .contact-list svg { width: 12px; height: 12px; flex: none; }
  /* Back: brand side */
  .back-photo {
    position: absolute; inset: 0;
    background: linear-gradient(180deg, var(--sky-top) 0%, #8cc6f0 30%, var(--sky-light) 45%, var(--sea-deep) 52%, var(--sea-turquoise) 62%, #bfe9e6 72%, var(--sand) 82%, #f1ede4 100%);
  }
  .back-brand {
    position: absolute; left: 26px; top: 138px;
    font-family: "Questrial", sans-serif; font-size: 22px; letter-spacing: .5px;
    color: var(--brand-grey);
  }
</style>
</head>
<body>
<main class="canvas">
  <section class="card card-front">
    <div class="front-photo" role="img" aria-label="Photo of a turquoise tropical bay with a wooden longtail boat on a white sand beach and limestone cliffs"></div>
    <div class="front-sand"></div>
    <p class="front-brand">Coral Breeze Escapes</p>
    <ul class="contact-list">
      <li>0437 912 654
        <svg viewBox="0 0 12 12" aria-hidden="true"><path fill="var(--icon-dark)" d="M2 4c0-1.5 1.5-2.5 4-2.5S10 2.5 10 4H8V3H4v1zM2.5 5h7l1 5h-9z"/></svg>
      </li>
      <li>delphine@coralbreezetrips.com
        <svg viewBox="0 0 12 12" aria-hidden="true"><rect x="1" y="3" width="10" height="7" fill="var(--icon-dark)"/><path d="M1 3l5 4 5-4" stroke="#fff" fill="none" stroke-width="1"/></svg>
      </li>
      <li>www.coralbreezeescapes.net
        <svg viewBox="0 0 12 12" aria-hidden="true"><circle cx="6" cy="6" r="5" fill="var(--icon-dark)"/><circle cx="6" cy="6" r="2.4" fill="none" stroke="#fff" stroke-width="1"/></svg>
      </li>
    </ul>
    <p class="contact-name">Delphine Orvak</p>
  </section>

  <section class="card card-back">
    <div class="back-photo" role="img" aria-label="Photo of a white cruise ship on a blue sea, a palm tree, and a couple in sun hats sitting on a white sand beach"></div>
    <p class="back-brand">Coral Breeze Escapes</p>
  </section>
</main>
</body>
</html>
```